Old Fashioned, Artisan Goat Milk Soap Label

We are branching out in our goat milk dairy into artisan goat milk soaps. High quality, yet an old fashioned feel. Simple yet elegant. Emphasis on the milk and its moisturizing, healing, softening, and superiority.
Purity in a simple design that harkens back to a quaint, earlier time where quality ingredients were valued as much as quality workmanship.
Perhaps a drop symbolizing the milk, or a bucket pouring into or out of the logo. We already have our farm logo, Quiet Hollow, and were thinking the soap would be "Simple Sue"
The labels will grace our liquid soap bottles and our bar soaps. 3.5" X 2.5"
The label color will be an antiqued ivory or other shade to convey a simpler time.

Reason: Realized that the contest length was short enough to scare away designers. Adding time to give entered designers time to create.

Target Market(s)

Upscale people looking to know where their products come from. People looking for better options, artisan products.

Requirements
Must have
• My project must have emphasis on the milk, old time feel, simple elegance
Nice to have
• Perhaps a drop symbolizing the milk, or a bucket pouring into or out of the logo. We already have our farm logo, Quiet Hollow, and were thinking the soap would be "Simple Sue"
• If you use a goat, please be aware that we have the breed Nubians that have long luxurious ears and don't have horns.

```html
<!DOCTYPE html>
<html lang="en">
<head>
<meta charset="utf-8">
<title>Simple Sue – Goat Milk Soap Label</title>
<link rel="stylesheet" href="https://fonts.googleapis.com/css2?family=Cinzel:wght@400;600&family=Poppins:wght@400;500&display=swap">
<style>
  :root {
    --page: #ffffff;
    --ivory: #f0e4cb;
    --ivory-edge: #e8d9bb;
    --rim: #5f5a55;
    --navy: #222656;
    --ink: #2a2a30;
    --flourish: #8a7358;
  }
  * { margin: 0; padding: 0; box-sizing: border-box; }
  html, body {
    width: 721px;
    height: 1200px;
    overflow: hidden;
    background: var(--page);
  }
  .canvas {
    position: relative;
    width: 721px;
    height: 1200px;
  }
  .label {
    position: absolute;
    left: 212px;
    top: 474px;
    width: 376px;
    height: 376px;
    border-radius: 50%;
    background: radial-gradient(circle at 50% 45%, var(--ivory) 60%, var(--ivory-edge) 100%);
    border: 3px solid var(--rim);
    text-align: center;
  }
  .farm-name {
    position: absolute;
    left: 0;
    right: 0;
    top: 42px;
    font-family: "Cinzel", serif;
    font-weight: 600;
    font-size: 27px;
    line-height: 36px;
    letter-spacing: 1px;
    color: var(--navy);
  }
  .flourish {
    position: absolute;
    left: 50%;
    transform: translateX(-50%);
    width: 160px;
    height: 20px;
    border-radius: 10px;
    background: radial-gradient(ellipse at center, var(--flourish) 0%, transparent 72%);
    opacity: 0.45;
  }
  .flourish--top { top: 136px; }
  .flourish--bottom { top: 214px; }
  .product-name {
    position: absolute;
    left: 0;
    right: 0;
    top: 164px;
    font-family: "Cinzel", serif;
    font-weight: 400;
    font-size: 42px;
    line-height: 48px;
    letter-spacing: 1px;
    color: var(--navy);
  }
  .product-type {
    position: absolute;
    left: 0;
    right: 0;
    top: 256px;
    font-family: "Poppins", sans-serif;
    font-weight: 400;
    font-size: 14px;
    line-height: 22px;
    color: var(--ink);
  }
  .benefits {
    position: absolute;
    left: 0;
    right: 0;
    top: 308px;
    font-family: "Poppins", sans-serif;
    font-weight: 500;
    font-size: 11px;
    line-height: 23px;
    color: var(--ink);
  }
</style>
</head>
<body>
  <main class="canvas">
    <section class="label">
      <div class="farm-name">Quiet Hollow</div>
      <div class="flourish flourish--top" role="img" aria-label="Decorative scroll flourish above the product name"></div>
      <h1 class="product-name">Simple Sue</h1>
      <div class="flourish flourish--bottom" role="img" aria-label="Decorative scroll flourish below the product name"></div>
      <p class="product-type">goat milk soaps</p>
      <p class="benefits">moisturizing, healing,<br>softening, and superiority.</p>
    </section>
  </main>
</body>
</html>
```